Ultra Distance Charity Bike Ride.

Hello.

I need a business card to pass to people whilst out on my charity bike ride.

I’m raising funds/awareness about mental health. My funds are going to Harbor Light. I have a link to my donation page in my instagram bio. My instagram page will also be a source for people to follow my adventures. My Instagram page is tomwelsk.

I would like to have this card not for just one trip, I’d like it to be something that I can use on future endeavors.

```html
<!DOCTYPE html>
<html lang="en">
<head>
<meta charset="utf-8">
<title>Tom Welsk – Charity Ride Card</title>
<link href="https://fonts.googleapis.com/css2?family=Open+Sans:wght@400;700&display=swap" rel="stylesheet">
<style>
  :root {
    --bg: #e6e4e1;
    --card: #ffffff;
    --teal: #1f8fb5;
    --panel: #2b96bf;
    --pink: #e0245f;
    --orange: #f0a42e;
    --white: #ffffff;
  }
  * { margin: 0; padding: 0; box-sizing: border-box; }
  html, body {
    width: 1200px; height: 962px; overflow: hidden;
    background: var(--bg);
    font-family: "Open Sans", sans-serif;
  }
  .canvas { position: relative; width: 1200px; height: 962px; }
  .card {
    position: absolute; left: 220px;
    width: 760px; height: 434px;
    background: var(--card);
    border-radius: 18px;
    overflow: hidden;
    box-shadow: 0 6px 18px rgba(0,0,0,0.15);
  }
  .card-front { top: 30px; }
  .card-back { top: 498px; }
  .card-shapes { position: absolute; inset: 0; }

  .front-brand {
    position: absolute; left: 0; right: 0; top: 150px;
    text-align: center; color: var(--teal);
    font-size: 64px; font-weight: 400; letter-spacing: 0.5px;
  }
  .front-handle {
    position: absolute; left: 0; right: 0; top: 290px;
    text-align: center; color: var(--teal);
    font-size: 26px; letter-spacing: 1.5px;
  }

  .back-brand {
    position: absolute; left: 30px; top: 180px; width: 300px;
    text-align: center; color: var(--teal);
    font-size: 42px; font-weight: 400;
  }
  .person {
    position: absolute; left: 430px; top: 92px;
    color: var(--white);
  }
  .person-name { font-size: 40px; font-weight: 700; line-height: 48px; }
  .person-role { font-size: 24px; font-weight: 400; line-height: 32px; }
  .contact {
    position: absolute; left: 430px; top: 200px;
    list-style: none; color: var(--white);
    font-size: 20px; line-height: 45px; white-space: nowrap;
  }
</style>
</head>
<body>
<main class="canvas">

  <section class="card card-front" aria-label="Card front">
    <svg class="card-shapes" width="760" height="434" viewBox="0 0 760 434" aria-hidden="true">
      <rect x="0" y="70" width="28" height="200" fill="var(--pink)"/>
      <polygon points="0,70 28,70 28,52" fill="var(--teal)"/>
      <rect x="732" y="180" width="28" height="220" fill="var(--orange)"/>
      <polygon points="732,180 760,180 760,162" fill="var(--teal)"/>
    </svg>
    <div class="front-brand">Harbor Light</div>
    <div class="front-handle">Follow the ride @tomwelsk</div>
  </section>

  <section class="card card-back" aria-label="Card back">
    <svg class="card-shapes" width="760" height="434" viewBox="0 0 760 434" aria-hidden="true">
      <polygon points="470,0 760,0 760,434 300,434 445,80" fill="var(--panel)"/>
      <polygon points="392,100 437,100 300,434 255,434" fill="var(--pink)"/>
      <!-- heart -->
      <path transform="translate(364 222)" fill="var(--white)"
            d="M0,9 C-14,0 -10,-10 -4,-10 C-1,-10 0,-7 0,-6 C0,-7 1,-10 4,-10 C10,-10 14,0 0,9 Z"/>
      <!-- pin -->
      <g transform="translate(345 267)" fill="var(--white)">
        <path d="M0,11 C-8,1 -8,-3 -8,-4 A8,8 0 0 1 8,-4 C8,-3 8,1 0,11 Z"/>
        <circle cy="-4" r="3" fill="var(--pink)"/>
      </g>
      <!-- at sign -->
      <g transform="translate(327 312)" fill="none" stroke="var(--white)" stroke-width="2.5">
        <circle r="4"/>
        <path d="M4,-2 V2 C4,5 9,5 9,0 A9,9 0 1 0 4,8"/>
      </g>
      <!-- link -->
      <g transform="translate(309 357) rotate(-45)" fill="none" stroke="var(--white)" stroke-width="2.5">
        <rect x="-11" y="-4" width="12" height="8" rx="4"/>
        <rect x="-1" y="-4" width="12" height="8" rx="4"/>
      </g>
    </svg>
    <div class="back-brand">Harbor Light</div>
    <div class="person">
      <div class="person-name">TOM WELSK</div>
      <div class="person-role">Charity Cyclist</div>
    </div>
    <ul class="contact">
      <li>Raising funds for Harbor Light</li>
      <li>Ultra Distance Charity Ride</li>
      <li>@tomwelsk – follow the ride</li>
      <li>Donate: link in bio</li>
    </ul>
  </section>

</main>
</body>
</html>
```